Business card design needed

We do excavation, cartage and contracting
I would quote like to have a picture of my digger as the whole back ground and the words on top. If that looks any good
Otherwise please feel free to come up with any other cool options

Cheers Marc

Industry/Entity Type

Business

Contact Information for Business Card

KRV Contracting
Excavation, Cartage, Contracting
Marcus Pellow
www.krv.co.nz
027 584 612
marc@krv.co.nz

```html
<!DOCTYPE html>
<html lang="en">
<head>
<meta charset="utf-8">
<title>KRV Contracting – Business Card</title>
<link rel="stylesheet" href="https://fonts.googleapis.com/css2?family=Arimo:wght@400;700&family=Tinos&display=swap">
<style>
  :root {
    --green: #1f5a2c;
    --white: #ffffff;
    --sky: #e4e9ea;
    --haze: #cfd6cc;
    --foliage: #b6c8a4;
    --foliage-deep: #a9bd98;
    --ground: #e6d6c3;
    --ground-deep: #dbc7b1;
  }
  * { margin: 0; padding: 0; box-sizing: border-box; }
  html, body { width: 1200px; height: 693px; overflow: hidden; background: var(--white); }
  .card { position: relative; width: 1200px; height: 693px; overflow: hidden; }

  .photo-area {
    position: absolute; inset: 0;
    background:
      radial-gradient(ellipse 420px 260px at 760px 250px, rgba(233, 200, 110, 0.45), rgba(233, 200, 110, 0) 70%),
      linear-gradient(180deg,
        var(--sky) 0%, var(--sky) 5%,
        var(--haze) 8%, var(--foliage) 12%,
        var(--foliage-deep) 30%, var(--foliage) 42%,
        var(--ground) 52%, var(--ground-deep) 100%);
  }

  .frame { position: absolute; inset: 0; }

  .services {
    position: absolute; left: 62px; top: 56px;
    font-family: "Arimo", Arial, sans-serif;
    font-size: 38px; line-height: 56px; color: var(--white);
    list-style: none;
  }

  .brand {
    position: absolute; left: 51px; top: 282px; width: 310px;
    text-align: center;
    font-family: "Arimo", Arial, sans-serif; font-weight: 700;
    font-size: 112px; line-height: 126px; letter-spacing: 4px; color: var(--white);
  }

  .contact {
    position: absolute; left: 66px; top: 500px;
    font-family: "Arimo", Arial, sans-serif;
    font-size: 31px; line-height: 44px; color: var(--white);
    font-style: normal;
  }

  .name {
    position: absolute; right: 73px; top: 509px;
    font-family: "Tinos", "Times New Roman", serif;
    font-size: 72px; line-height: 80px; color: var(--green);
  }
</style>
</head>
<body>
  <div class="card">
    <div class="photo-area" role="img" aria-label="Photograph of a yellow excavator digging on a gravel hillside above a river valley, faded as a background"></div>

    <svg class="frame" width="1200" height="693" viewBox="0 0 1200 693" aria-hidden="true">
      <rect x="300" y="510" width="900" height="77" fill="var(--white)"/>
      <rect x="300" y="510" width="900" height="5" fill="var(--green)"/>
      <rect x="300" y="582" width="900" height="5" fill="var(--green)"/>
      <path d="M0 0 H307 V100 C431 210 456 470 316 650 V693 H0 Z" fill="var(--white)"/>
      <path d="M0 0 H291 V100 C415 210 440 470 300 650 V693 H0 Z" fill="var(--green)"/>
    </svg>

    <ul class="services">
      <li>Contracting</li>
      <li>Excavation</li>
      <li>Cartage</li>
    </ul>

    <div class="brand">KRV</div>

    <address class="contact">
      <div class="contact-web">www.krv.co.nz</div>
      <div class="contact-phone">027-584-612</div>
      <div class="contact-email">marc@krv.co.nz</div>
    </address>

    <div class="name">Marcus Pellow</div>
  </div>
</body>
</html>
```